Plumweave Inc. Website & Korvix Apps Landing Pages

We need a web site design for our company. We develop software and do various consultant projects for our clients. Our products focus on the mobile platform, mainly the Korvix (business, games, social, etc.). We want to communicate that our software is simple and good as candy. The web pages should be fun to look at not loosing seriousness and credibility. Web 2.0 style and 960 grid system a must. We are opened to any overall site colour scheme suggestions (look at the sites we like below).

Must haves:
- Our logo should be seen on the site and look great on it :-) (preview attached below)
- Main home page and app landing page.
- Section links/tabs on the home page (home,apps,support,blog,contact,about)
- No text in images
- Style sheet

Looks we like:
- http://x7k3lmq9pwrtzv.pixelmoorvault.net/412_Zelto_Site/final_large.jpg
- http://x7k3lmq9pwrtzv.pixelmoorvault.net/Premium_71_Illustrative_Korvix_Landing_Page/final.jpg
- http://grelmwick.com/
- http://dorniply.ca/
- http://quatzel.com/

Industry/Entity Type

Business

Requirements
Must have
• - Company logo should look great on pages.
• - Main home page and app landing page.
• - Section links/tabs on the home page (home,apps,support,blog,contact,about)
• - Web 2.0 style.
• - 960 grid system (12 col, 16 col).
• - Sliced ann optmized
• - Exported in all major formats (psd,ai,eps,png,jpeg,etc)
• - Style sheet
Should not have
• - Text in images

```html
<!DOCTYPE html>
<html lang="en">
<head>
<meta charset="utf-8">
<title>Plumweave – Carve Mate</title>
<link href="https://fonts.googleapis.com/css2?family=Ubuntu:wght@400;500&family=Arimo:wght@400;700&display=swap" rel="stylesheet">
<style>
:root{
  --dark:#2b2e2f;
  --dark-3:#1d1f20;
  --accent-red:#c8200c;
  --light:#f3f3f3;
  --text:#3a3a3a;
  --muted:#8b9092;
  --white:#ffffff;
  --line:#3c4042;
}
*{box-sizing:border-box;margin:0;padding:0}
html,body{width:1200px;height:1134px;overflow:hidden}
body{position:relative;background:var(--light);font-family:"Arimo",Arial,sans-serif;color:var(--text)}
.abs{position:absolute}
.site-header{left:0;top:0;width:1200px;height:92px;background:linear-gradient(#3a3d3e,var(--dark));border-bottom:2px solid #1a1c1d}
.logo{left:121px;top:26px;font-family:"Ubuntu",sans-serif;font-size:34px;font-weight:500;color:var(--white);letter-spacing:.5px;display:flex;align-items:center;gap:10px}
.logo .dot{width:14px;height:14px;border-radius:50%;background:var(--accent-red)}
.callus{right:122px;top:9px;font-size:12px;color:#8a8f91}
.callus b{color:#b5b9bb;font-weight:400}
.main-nav{top:38px;left:523px;display:flex}
.main-nav a{font-size:14px;color:var(--white);text-decoration:none;padding:5px 12px;border-radius:8px;margin-right:26px}
.main-nav a.active{background:#4a4e50}
.main-nav a:last-child{margin-right:0}
.hero{left:0;top:92px;width:1200px;height:346px;background:radial-gradient(circle at 72% 40%,rgba(255,190,30,.9) 0%,rgba(247,124,14,.6) 30%,transparent 60%),linear-gradient(165deg,#fa8c14 0%,#ef6010 40%,#da330b 75%,#c81f0a 100%)}
.hero h1{left:120px;top:78px;font-family:"Ubuntu",sans-serif;font-weight:500;font-size:34px;line-height:36px;color:var(--white)}
.hero .rule{left:120px;top:175px;width:400px;height:1px;background:rgba(255,255,255,.35)}
.hero .sub{left:120px;top:200px;font-family:"Ubuntu",sans-serif;color:var(--white);font-size:18px}
.hero .sub2{left:120px;top:228px;font-family:"Ubuntu",sans-serif;color:var(--white);font-size:23px}
.dots{left:120px;top:306px;display:flex;gap:20px}
.dots span{width:16px;height:16px;border-radius:50%;background:rgba(150,20,0,.35);box-shadow:inset 0 1px 2px rgba(0,0,0,.3)}
.dots span.on{background:radial-gradient(circle,#fff 0,#ff9a70 30%,#c82a0a 70%)}
.hero-art{left:630px;top:30px;width:310px;height:296px;border-radius:24px;background:linear-gradient(135deg,#2a2a2a,#555 50%,#1e1e1e)}
.page-title{left:121px;top:462px;font-family:"Ubuntu",sans-serif;font-weight:400;font-size:29px;color:#222}
.page-title .slash{color:#bbb}
.page-title .app{color:var(--accent-red)}
.intro{left:120px;top:510px;width:376px;font-size:12.5px;line-height:22px;text-align:justify;color:#444;letter-spacing:.2px}
.divider{left:120px;top:730px;width:376px;height:1px;background:#ddd}
.coming{left:120px;top:748px;font-size:11px;line-height:18px;color:#333}
.coming h3{font-size:13px;font-weight:700;margin-bottom:1px}
.showcase{left:531px;top:469px;width:549px;height:380px;background:#f7f7f7;border:1px solid #e6e6e6;border-radius:8px}
.showcase .split{left:249px;top:0;width:1px;height:378px;background:#e5e5e5}
.shot{left:50px;top:26px;width:152px;height:292px;border-radius:18px;background:linear-gradient(#3c3c3c,#111);border:2px solid #ccc}
.shot .screen{position:absolute;left:9px;top:48px;width:130px;height:196px;background:linear-gradient(#b98a4e,#7d5a2a)}
.shot .home{position:absolute;left:62px;top:256px;width:24px;height:24px;border-radius:50%;border:2px solid #555}
.slider{left:51px;top:342px;width:150px;height:10px;border-radius:5px;background:#ddd}
.slider i{position:absolute;left:50px;top:0;width:26px;height:10px;border-radius:5px;background:var(--accent-red)}
.shot-caption{left:0;width:250px;top:359px;text-align:center;font-size:11px;color:#777}
.features{left:278px;top:25px;width:247px;height:329px;border-radius:8px;background:var(--dark);border:2px solid #191b1c;padding:20px 22px}
.features h2{font-family:"Ubuntu",sans-serif;font-weight:400;font-size:26px;color:var(--white);margin-bottom:6px}
.features p{font-size:11px;line-height:19px;color:#d8d8d8}
.shadow{left:560px;top:853px;width:500px;height:16px;border-radius:50%;background:radial-gradient(ellipse,rgba(0,0,0,.18),transparent 70%)}
.site-footer{left:0;top:890px;width:1200px;height:207px;background:var(--dark);border-top:2px solid #1b1d1e}
.col-title{font-family:"Ubuntu",sans-serif;font-weight:400;font-size:19px;color:var(--white)}
.links{font-size:12px;line-height:24px;color:var(--muted);letter-spacing:.4px;list-style:none}
.vline{width:1px;height:140px;background:var(--line)}
.field{height:26px;border-radius:8px;background:#222526;border:1px solid #474b4d;font-size:12px;color:#aaa;padding:6px 11px}
.btn{height:26px;border-radius:8px;background:#3d4143;border:1px solid #505456;color:#ddd;font-size:12px;font-weight:700;padding:6px 13px}
.unsub{font-size:11px;color:#bbb;text-decoration:underline}
.follow{font-family:"Ubuntu",sans-serif;font-size:17px;color:var(--white)}
.social{display:flex;gap:8px}
.social span{width:19px;height:19px;border-radius:3px;background:#c6c9ca}
.bottom-bar{left:0;top:1097px;width:1200px;height:37px;background:var(--dark-3)}
.copy{left:117px;top:12px;font-size:11px;color:#8a8e90}
.badge{top:11px;width:66px;height:15px;border:1px solid #666;background:#3a3d3e}
.legal{right:120px;top:12px;font-size:11px;color:#8a8e90}
</style>
</head>
<body>
<header class="site-header abs">
  <div class="logo abs"><span class="dot"></span>Plumweave</div>
  <div class="callus abs">Call Us <b>+00 4821 7730</b></div>
  <nav class="main-nav abs">
    <a href="#">HOME</a><a href="#" class="active">APPS</a><a href="#">SUPPORT</a><a href="#">BLOG</a><a href="#">CONTACT</a><a href="#">ABOUT</a>
  </nav>
</header>

<section class="hero abs">
  <h1 class="abs">Mobile Application<br>Development</h1>
  <div class="rule abs"></div>
  <p class="sub abs">We make&nbsp; Professional apps for Mobile Phones</p>
  <p class="sub2 abs">Quick and Easy.</p>
  <div class="dots abs"><span></span><span></span><span class="on"></span><span></span><span></span></div>
  <div class="hero-art abs" role="img" aria-label="Three smartphones showing app home screens"></div>
</section>

<h2 class="page-title abs">Applications <span class="slash">/</span> <span class="app">Carve Mate</span></h2>
<div class="intro abs">
  <p>Carve Mate is the ultimate meat cooking application for professionals and aspiring home master chefs! Impress your friends at your next BBQ with the unique Cooking Timer and mouth-watering exclusive recipes from one of the world's leading Charcuterie Chefs.</p>
  <p>Carve Mate's success has led to mentions and articles in such publications as The Harbor Ledger, The Eastcoast Morning Post, The Southlander, AppBasket, GrillyApps, BrightApps and more!</p>
</div>
<div class="divider abs"></div>
<div class="coming abs">
  <h3>What's coming soon in Version 1.1?</h3>
  - NEW 'Recipe Timer' for every recipe!<br>
  - U.S. names for all cuts!<br>
  - Additional cooking methods for the timer!<br>
  - Additional weights for the timer!
</div>

<section class="showcase abs">
  <div class="split abs"></div>
  <div class="shot abs"><div class="screen" role="img" aria-label="App screenshot with cooking timer on a wooden board"></div><div class="home"></div></div>
  <div class="slider abs"><i></i></div>
  <div class="shot-caption abs">screenshot (8)</div>
  <div class="features abs">
    <h2>Features</h2>
    <p>- Beautifully crafted graphics feel right at home in the kitchen.<br>
    - Select a cut of meat from the butcher's blackboard, or choose from a list of common meat cuts.<br>
    - Over 30 exclusive mouth-watering recipes from one of the world's finest charcuterie chefs - Lucien Marvaux.<br>
    - Never burn your meat again when you use our handy cooking timer<br>
    - pick the weight, 'doneness' and cooking style and you will be reminded when you need to flip the meat!</p>
  </div>
</section>
<div class="shadow abs"></div>

<footer class="site-footer abs">
  <h3 class="col-title abs" style="left:121px;top:24px">Technology Expertise</h3>
  <ul class="links abs" style="left:123px;top:54px">
    <li>Korvix Development</li><li>Zelvo, Quarn, Brisk</li><li>Mobile App Development</li><li>Game Development</li><li>Business Software Development</li>
  </ul>
  <div class="vline abs" style="left:376px;top:28px"></div>
  <h3 class="col-title abs" style="left:407px;top:24px">Solutions</h3>
  <ul class="links abs" style="left:409px;top:54px">
    <li>Mobile Application Development</li><li>Application Support</li><li>Mobile Application Upgrade</li><li>Navigation App Support</li><li>Mobile Application Outsource</li>
  </ul>
  <div class="vline abs" style="left:679px;top:28px"></div>
  <h3 class="col-title abs" style="left:721px;top:24px">Newsletter</h3>
  <div class="field abs" style="left:719px;top:57px;width:176px">Name</div>
  <div class="field abs" style="left:903px;top:57px;width:176px">E-mail</div>
  <div class="btn abs" style="left:719px;top:95px">Subscribe</div>
  <div class="unsub abs" style="left:1013px;top:100px">Unsubscribe</div>
  <div class="abs" style="left:719px;top:137px;width:360px;height:1px;background:var(--line)"></div>
  <div class="follow abs" style="left:721px;top:154px">Follow Us!</div>
  <div class="social abs" style="left:810px;top:155px"><span></span><span></span><span></span><span></span></div>
</footer>

<div class="bottom-bar abs">
  <div class="copy abs">Copyright © 2010 Plumweave. All rights reserved.</div>
  <div class="badge abs" style="left:377px"></div>
  <div class="badge abs" style="left:446px;width:97px"></div>
  <div class="legal abs">Privacy Policy &nbsp;|&nbsp; Contact Us &nbsp;|&nbsp; Disclaimer &nbsp;|&nbsp; Terms of Use</div>
</div>
</body>
</html>
```